Rocket business card

Modern business card design, use of color is good with clean space too.

Things to include on card:

Quote: I add fuel to your optometry practice

- Eyewear Sales
- Admin Duties
- Revenue Collection
- Leadership
- Tech Adoption
- COGS Reduction
- Product Sourcing
-Medical Growth

Dalton Vessey, CEO
Glint Harbor
Text Me! 847-302-1964
dalton@glintharbor.example

```html
<!DOCTYPE html>
<html lang="en">
<head>
<meta charset="utf-8">
<title>Glint Harbor – Business Card</title>
<link rel="stylesheet" href="https://fonts.googleapis.com/css2?family=Raleway:wght@400&family=Open+Sans:wght@300;400&family=Oswald:wght@600&display=swap">
<style>
  :root {
    --backdrop: #222629;
    --card-light: #f7f7f7;
    --card-shade: #d9d9d9;
    --ink: #3d3d3d;
    --ink-soft: #4a4a4a;
    --accent-red: #d62f2a;
    --accent-orange: #ef8a1c;
    --accent-amber: #f2a51f;
    --back-left: #d88a1c;
    --back-right: #e03e2c;
    --white: #ffffff;
  }
  html, body {
    margin: 0;
    width: 1200px;
    height: 1176px;
    overflow: hidden;
    background: var(--backdrop);
  }
  .canvas {
    position: relative;
    width: 1200px;
    height: 1176px;
  }
  .card {
    position: absolute;
    left: 280px;
    width: 617px;
    height: 352px;
    border-radius: 22px;
    overflow: hidden;
    box-shadow: 0 10px 24px rgba(0,0,0,0.45);
  }
  .card--front {
    top: 190px;
    background: linear-gradient(200deg, var(--white) 0%, var(--card-light) 35%, var(--card-shade) 100%);
  }
  .card--back {
    top: 590px;
    background: linear-gradient(90deg, var(--back-left) 0%, #e36a23 55%, var(--back-right) 100%);
  }

  /* front */
  .brand {
    position: absolute;
    right: 44px;
    top: 92px;
    display: flex;
    align-items: center;
    gap: 12px;
    font-family: "Raleway", sans-serif;
    font-size: 30px;
    letter-spacing: 2px;
    color: #1a1a1a;
  }
  .brand__dot {
    width: 22px;
    height: 22px;
    border-radius: 50%;
    background: var(--accent-orange);
  }
  .holder__name {
    position: absolute;
    left: 36px;
    top: 150px;
    margin: 0;
    font-family: "Raleway", sans-serif;
    font-weight: 400;
    font-size: 25px;
    color: var(--ink);
  }
  .holder__role {
    position: absolute;
    left: 36px;
    top: 182px;
    font-family: "Raleway", sans-serif;
    font-size: 15px;
    color: var(--accent-orange);
  }
  .holder__rule {
    position: absolute;
    left: 78px;
    right: 0;
    top: 190px;
    height: 3px;
    background: linear-gradient(90deg, var(--accent-red) 0%, #d8402a 50%, var(--accent-amber) 52%, var(--accent-amber) 100%);
  }
  .contacts {
    position: absolute;
    left: 36px;
    top: 237px;
    margin: 0;
    padding: 0;
    list-style: none;
    font-family: "Open Sans", sans-serif;
    font-size: 15px;
    color: var(--ink-soft);
  }
  .contacts li {
    display: flex;
    align-items: center;
    gap: 10px;
    height: 27px;
  }
  .contacts svg { width: 14px; height: 14px; flex: none; }
  .contacts__note { font-size: 9px; vertical-align: 6px; margin-left: 2px; }

  /* back */
  .halo {
    position: absolute;
    left: 102px;
    top: -14px;
    width: 414px;
    height: 414px;
    border-radius: 50%;
    background: linear-gradient(90deg, #c52f2b 0%, #e2642a 50%, var(--accent-amber) 100%);
  }
  .tagline {
    position: absolute;
    left: 0;
    right: 0;
    top: 55px;
    margin: 0;
    text-align: center;
    font-family: "Oswald", sans-serif;
    font-weight: 600;
    font-size: 16px;
    line-height: 25px;
    color: var(--white);
    transform: translateX(-4px);
  }
  .services {
    position: absolute;
    left: 0;
    right: 0;
    top: 268px;
    margin: 0;
    text-align: center;
    font-family: "Open Sans", sans-serif;
    font-weight: 300;
    font-size: 14.5px;
    line-height: 26px;
    color: rgba(255,255,255,0.9);
  }
  .services .sep { margin: 0 9px; }
</style>
</head>
<body>
<main class="canvas">

  <section class="card card--front" aria-label="Card front">
    <div class="brand"><span class="brand__dot"></span>GLINT HARBOR</div>

    <h1 class="holder__name">Dalton Vessey</h1>
    <span class="holder__role">CEO</span>
    <div class="holder__rule"></div>

    <ul class="contacts">
      <li>
        <svg viewBox="0 0 14 14" aria-hidden="true"><rect x="4" y="1" width="6" height="12" rx="1.2" fill="none" stroke="#e0452a" stroke-width="1.4"/><line x1="6" y1="11" x2="8" y2="11" stroke="#e0452a" stroke-width="1.2"/></svg>
        <span>847-302-1964<span class="contacts__note">Text Me!</span></span>
      </li>
      <li>
        <svg viewBox="0 0 14 14" aria-hidden="true"><rect x="1" y="3" width="12" height="8" fill="#e6652a"/><polyline points="1,3 7,8 13,3" fill="none" stroke="#fff" stroke-width="1"/></svg>
        <span>dalton@glintharbor.example</span>
      </li>
      <li>
        <svg viewBox="0 0 14 14" aria-hidden="true" fill="none" stroke="#e6752a" stroke-width="1.1"><circle cx="7" cy="7" r="5.5"/><ellipse cx="7" cy="7" rx="2.4" ry="5.5"/><line x1="1.5" y1="7" x2="12.5" y2="7"/><line x1="2.5" y1="4" x2="11.5" y2="4"/><line x1="2.5" y1="10" x2="11.5" y2="10"/></svg>
        <span>glintharbor.example</span>
      </li>
    </ul>
  </section>

  <section class="card card--back" aria-label="Card back">
    <div class="halo"></div>
    <p class="tagline">I<br>add<br>fuel<br>to your<br>optometry<br>practice</p>
    <p class="services">
      Eyewear Sales<span class="sep">I</span>Admin Duties<span class="sep">I</span>Revenue Collection<span class="sep">I</span>Leadership<br>
      Tech Adoption<span class="sep">I</span>COGS Reduction<span class="sep">I</span>Product Sourcing<span class="sep">I</span>Medical Growth
    </p>
  </section>

</main>
</body>
</html>
```